Business cards for Stormsail Consulting (Leadership & Performance Coaching and HR Consulting)

I have a logo (although I'm open to new ideas) and I need this added to a business card. Ultimately, I will also need help with a website. This is an independent consulting firm that is focuses on Leadership, Performance, Executive Coaching and Talent.
Google the story about "one storm, one sailor" ... hence the 1S1S

Target Market(s)

My clients, CEOs, CHROs, COOs

Contact Information for Business Card

Dana K. Wolfe
President
214.553.0871
dwolfe52@ventomail.net
www.1S1SConsulting.com
3918 Hollowmere Dr., Cedarbrook, TX 75418

Font styles to use
Serif
Sans Serif

Colors
ec1f27
0455a3

Requirements
Must have
• Color, be professional
Nice to have
• Something that pops off the card
Should not have
• Be boring.

```html
<!DOCTYPE html>
<html lang="en">
<head>
<meta charset="utf-8">
<title>Stormsail Consulting — Business Cards</title>
<link rel="stylesheet" href="https://fonts.googleapis.com/css2?family=Roboto:wght@400;500;700&display=swap">
<style>
  :root {
    --backdrop: #d9d4cc;
    --card: #040608;
    --brand-red: #e31e26;
    --brand-blue: #3a4fa3;
    --sky-blue: #4aa8e0;
    --body-text: #d8d8d8;
    --shadow: rgba(0, 0, 0, 0.35);
  }
  * { margin: 0; padding: 0; box-sizing: border-box; }
  html, body {
    width: 1125px;
    height: 1200px;
    overflow: hidden;
    background: var(--backdrop);
    font-family: "Roboto", Arial, sans-serif;
  }
  .sheet { position: relative; width: 1125px; height: 1200px; }
  .card {
    position: absolute;
    left: 170px;
    width: 826px;
    height: 470px;
    background: var(--card);
    box-shadow: 0 6px 14px var(--shadow);
    overflow: hidden;
  }
  .card--front { top: 106px; }
  .card--back { top: 639px; }

  .brand-mark {
    position: absolute;
    border-radius: 50%;
    background: var(--brand-red);
  }
  .card--front .brand-mark { left: 152px; top: 45px; width: 112px; height: 112px; }

  .brand-name {
    position: absolute;
    color: var(--brand-red);
    font-weight: 700;
    font-size: 28px;
    line-height: 32px;
    letter-spacing: 0.3px;
    text-transform: uppercase;
    white-space: nowrap;
  }
  .card--front .brand-name { left: 54px; top: 176px; }

  .tagline {
    position: absolute;
    left: 55px;
    top: 212px;
    color: var(--sky-blue);
    font-size: 15px;
    line-height: 18px;
    font-weight: 500;
    letter-spacing: 1.6px;
    text-transform: uppercase;
    white-space: nowrap;
  }

  .address {
    position: absolute;
    left: 54px;
    top: 315px;
    color: var(--body-text);
    font-size: 19px;
    line-height: 25px;
    font-style: normal;
  }
  .contact-list {
    position: absolute;
    left: 54px;
    top: 377px;
    list-style: none;
    color: var(--body-text);
    font-size: 19px;
    line-height: 25px;
  }
  .contact-list li { display: flex; align-items: center; gap: 11px; }
  .contact-icon { width: 18px; height: 18px; fill: var(--brand-blue); flex: none; }

  .person {
    position: absolute;
    right: 44px;
    top: 98px;
    text-align: right;
  }
  .person__name {
    color: var(--brand-blue);
    font-size: 30px;
    font-weight: 700;
    line-height: 32px;
    text-transform: uppercase;
  }
  .person__role {
    color: var(--brand-red);
    font-size: 20px;
    font-weight: 500;
    line-height: 22px;
    text-transform: uppercase;
    letter-spacing: 0.5px;
  }
  .accent-bar {
    position: absolute;
    right: 0;
    top: 100px;
    width: 9px;
    height: 48px;
    background: var(--brand-red);
  }

  .card--back .brand-mark { left: 611px; top: 246px; width: 110px; height: 110px; }
  .card--back .brand-name { right: 50px; top: 366px; font-size: 24px; line-height: 28px; }
  .website {
    position: absolute;
    right: 50px;
    top: 410px;
    color: var(--body-text);
    font-size: 20px;
    line-height: 24px;
    letter-spacing: 0.5px;
  }
</style>
</head>
<body>
<main class="sheet">
  <section class="card card--front" aria-label="Business card front">
    <div class="brand-mark" aria-hidden="true"></div>
    <h1 class="brand-name">Stormsail Consulting</h1>
    <p class="tagline">Leadership and Performance</p>

    <div class="person">
      <p class="person__name">Dana K. Wolfe</p>
      <p class="person__role">President</p>
    </div>
    <div class="accent-bar" aria-hidden="true"></div>

    <address class="address">3918 Hollowmere Dr.<br>Cedarbrook, TX 75418</address>
    <ul class="contact-list">
      <li>
        <svg class="contact-icon" viewBox="0 0 24 24" aria-hidden="true"><path d="M6.6 10.8c1.4 2.8 3.8 5.1 6.6 6.6l2.2-2.2c.3-.3.7-.4 1-.2 1.1.4 2.3.6 3.6.6.6 0 1 .4 1 1V20c0 .6-.4 1-1 1C10.6 21 3 13.4 3 4c0-.6.4-1 1-1h3.5c.6 0 1 .4 1 1 0 1.3.2 2.5.6 3.6.1.3 0 .7-.2 1l-2.3 2.2z"/></svg>
        <span>214.553.0871</span>
      </li>
      <li>
        <svg class="contact-icon" viewBox="0 0 24 24" aria-hidden="true"><path d="M2 5h20v14H2V5zm2 2v.5l8 5 8-5V7H4zm0 2.8V17h16V9.8l-8 5-8-5z"/></svg>
        <span>dwolfe52@ventomail.net</span>
      </li>
    </ul>
  </section>

  <section class="card card--back" aria-label="Business card back">
    <div class="brand-mark" aria-hidden="true"></div>
    <p class="brand-name">Stormsail Consulting</p>
    <p class="website">StormsailConsulting.com</p>
  </section>
</main>
</body>
</html>
```